Power Point Template Kalmora sustainability consulting

Please note:
We are not looking for new design proposals anymore since we've already received templetes from two designers that we really like. We are currently discussing possible changes with them and will make a final decision soon. Thank you very much.

(find english description below)
We are a small German start-up that offers sustainability consulting. For presentations of results, our company presentation, proposals, lectures, etc., we need a PowerPoint template that matches our logo. We come from classic management consulting / strategy consulting and also deal with facts and figures in sustainability consulting. Therefore, the template should not be too fancy and should not only consist of photos. But it shouldn't be a completely sober template either. Our logo with the green leaves for sustainability (three leaves for KALmora) and the white bar chart (with the dynamic swing upwards) reflects our attitude well, where we see ourselves on the range from playful to sober and classic to modern.

It might be nice for the template to include the shape of one of the leaves (from the logo). Also, the logo should appear in a corner of each slide. The colors from the logo (see appendix) should be partially reflected in the presentation. We can also imagine a gold-brown tone (see website www.kalmora-consulting.example) or a coral tone as a contrast. (Attention - the website is not final yet).

For a first suggestion, it is sufficient to suggest three to four slides (cover sheet, chapter/separation slide, text slide, data slide). We will then mark drafts that we like. In total, we would then need about 6-10 more slide templates, e.g. about us, team, slide for a statement, 2-3 data charts (pie, bar, column), top 3 - 5 list, timeline, contact (more slides are welcome ).

We are a small German start-up offering sustainability consulting. We need a power point template for result presentations, our company presentation, proposals, lectures etc. The template should be aligned with our logo. Our background lies in classic management consulting / strategy consulting and we also deal with facts and figures in sustainability consulting. Therefore, the template should not be too playful and not only consist of photos. But it should also not be a completely clear template. Our logo with the green leaves for sustainability (three leaves for KALmora) and the white bar chart (with the dynamic upward swing) reflects our attitude well, where we see ourselves on the range from playful to down-to-earth and classic to modern .

For the template, it might be nice to incorporate the shape of one of the leaves (from the logo). Also, the logo should show up in one corner on each slide. Some of the colors from the logo (see attachment) should be reflected in the presentation. We could also think of a gold-brown tone (see website www.kalmora-consulting.example) or a coral tone for contrast. (Attention - the website is not final yet).

For a first proposal it is quite sufficient to suggest us three to four slides (cover page, chapter/separation slide, text slide, data slide). We will then mark the drafts that we like. In total we would need about 6-10 more slide templates, eg About us, Team, slide for a statement, 2-3 data charts (pie, bar, column), Top 3 - 5 List, Timeline, Contact (more slides are welcome).

Target Market(s)

Corporations, large companies and SMEs

Industry/Entity Type

Unternehmensberatung, Nachhaltigkeitsberatung

Font styles to use
Sans Serif
Other font styles liked:
• Calibri

Colors
00AB8E
00BBA5
67D7C9
C6EFE9
E9F9F6

Requirements
Must have
• see description (e.g. the colors of our logo)
Nice to have
• see description (e.g. elements of the logo included)
Should not have
• see description

```html
<!DOCTYPE html>
<html lang="en">
<head>
<meta charset="utf-8">
<title>Kalmora – Presentation Template Overview</title>
<link rel="stylesheet" href="https://fonts.googleapis.com/css2?family=Montserrat:wght@400;500;600;700;800&display=swap">
<style>
:root{
  --stage:#1a1212;
  --green-dark:#3f7212;
  --green:#4c7f18;
  --green-mid:#6a9e2e;
  --lime:#a9c94c;
  --lime-pale:#d7e47d;
  --ink:#2a2a2a;
  --grey:#8b8b8b;
  --grey-light:#f2f2f2;
  --white:#ffffff;
}
*{box-sizing:border-box;margin:0;padding:0}
html,body{width:1200px;height:704px;overflow:hidden;background:var(--stage);font-family:"Montserrat",Arial,sans-serif}
.board{position:relative;width:1200px;height:704px}
.slide{position:absolute;width:369px;height:207px;overflow:hidden;background:var(--white);color:var(--ink)}
.slide.is-green{background:var(--green-dark);color:var(--white)}
.col-1{left:30px}.col-2{left:416px}.col-3{left:800px}
.row-1{top:18px}.row-2{top:246px}.row-3{top:474px}
.abs{position:absolute}

/* brand */
.brand{position:absolute;top:7px;right:6px;display:flex;align-items:center;gap:3px;line-height:1}
.brand-dot{width:9px;height:9px;border-radius:50%;background:var(--lime)}
.brand-name{font-size:11px;font-weight:500;color:#6e6e6e}
.is-green .brand-name{color:var(--white)}

/* footer */
.footer{position:absolute;left:0;right:0;bottom:0;height:10px;background:var(--green-mid)}
.footer-tab{position:absolute;right:0;bottom:0;height:10px;width:55px;background:var(--lime);clip-path:polygon(8px 0,100% 0,100% 100%,0 100%);font-size:3.4px;color:var(--white);display:flex;align-items:center;justify-content:center}

/* type */
.title{font-weight:700;font-size:11px;line-height:1.2;text-transform:uppercase;letter-spacing:.1px}
.title .accent{color:var(--green-mid)}
.is-green .title .accent{color:var(--lime-pale)}
.body{font-size:3.3px;line-height:1.75;color:#444}
.is-green .body{color:#e6efdb}

/* cover */
.cover{background:linear-gradient(120deg,#fafafa,#ececec)}
.cover-band{position:absolute;inset:0}
.cover-brand{position:absolute;left:21px;top:82px;display:flex;align-items:center;gap:5px;line-height:1}
.cover-brand .brand-dot{width:22px;height:22px}
.cover-brand .brand-name{font-size:23px;font-weight:400;color:#6a6a6a}
.cover-title{position:absolute;left:21px;top:126px;font-size:12px;font-weight:800;color:var(--green)}
.cover-body{position:absolute;left:21px;top:143px;width:150px}

/* progress */
.progress{position:absolute;left:22px;width:107px}
.progress-track{height:2px;background:#d6d6d6;border-radius:1px;position:relative}
.progress-fill{position:absolute;left:0;top:0;height:2px;background:var(--green);border-radius:1px}
.progress-badge{position:absolute;top:-7px;transform:translateX(-50%);font-size:2.6px;background:var(--green);color:#fff;border-radius:3px;padding:1px 2px}
.progress-year{font-size:3.4px;margin-top:3px;color:#333}
.photo{position:absolute}

/* checklist */
.checklist{position:absolute;display:flex;flex-direction:column;gap:8.5px}
.check{display:flex;gap:4px;align-items:flex-start;width:105px}
.check-box{width:5px;height:5px;border:1px solid var(--green);flex:none;margin-top:1px;position:relative}
.check-box::after{content:"";position:absolute;left:1px;top:1px;width:1.2px;height:1.2px;background:var(--green)}

/* process */
.step{position:absolute;width:100px}
.step-tag{width:28px;height:13px;background:var(--lime-pale);clip-path:polygon(0 0,78% 0,100% 50%,78% 100%,0 100%,14% 50%);color:var(--green-dark);font-size:5.5px;font-weight:600;display:flex;align-items:center;justify-content:center}
.step-title{font-size:4.2px;font-weight:700;margin:4px 0 1px;text-transform:uppercase}

/* testimonials */
.quote{position:absolute;width:85px;display:flex;gap:5px;align-items:flex-start}
.quote.is-left{flex-direction:row-reverse;text-align:right}
.quote-avatar{width:15px;height:15px;border-radius:50%;background:#a8a8a8;flex:none}
.quote-name{font-size:4.4px;font-weight:600;margin-bottom:1px}
.quote .body{font-size:3px;line-height:1.7}
.rating{position:absolute;left:154px;top:98px;width:62px;height:62px}
.rating-value{position:absolute;left:154px;top:98px;width:62px;height:62px;display:flex;align-items:center;justify-content:center;font-size:11px;font-weight:700;color:var(--green)}

/* legend */
.legend{position:absolute;display:flex;gap:14px;font-size:4px}
.legend span{display:flex;align-items:center;gap:2px}
.legend i{width:4px;height:4px;border-radius:50%;border:1px solid}

/* numbered list */
.numbered{position:absolute;display:flex;flex-direction:column;gap:7px;width:130px}
.numbered li{list-style:none;display:flex;gap:8px;align-items:center}
.num{width:9px;height:9px;border-radius:50%;background:#2f5a0c;font-size:2.8px;display:flex;align-items:center;justify-content:center;flex:none}

/* thank you */
.thanks-frame{position:absolute;left:89px;top:67px;width:192px;height:70px}
.thanks-text{position:absolute;left:89px;top:86px;width:192px;text-align:center;font-size:22px;font-weight:800;color:var(--white)}
.socials{position:absolute;left:166px;top:164px;display:flex;gap:2px}
.socials i{width:8px;height:8px;border-radius:50%;background:var(--lime-pale)}
</style>
</head>
<body>
<main class="board">

  <!-- Cover -->
  <section class="slide cover col-1 row-1">
    <svg class="cover-band" viewBox="0 0 369 207" aria-hidden="true">
      <polygon points="369,0 369,207 190,207" fill="#c4dc72"/>
      <polygon points="230,0 369,0 369,150 215,207 175,207" fill="#4c7f18"/>
      <polygon points="280,0 369,0 369,90 250,207 215,207" fill="#6a9e2e"/>
    </svg>
    <div class="cover-brand"><span class="brand-dot"></span><span class="brand-name">Kalmora</span></div>
    <h1 class="cover-title">PROJECT TITLE HERE</h1>
    <p class="body cover-body">Excepteur sint occaecat cupidatat non proident, sunt in culpa qui officia deserunt mollit anim id est laborum. Sed ut perspiciatis unde omnis iste natus error sit voluptatem accusantium doloremque laudantium.</p>
  </section>

  <!-- Progress -->
  <section class="slide col-2 row-1">
    <div class="brand"><span class="brand-dot"></span><span class="brand-name">Kalmora</span></div>
    <h2 class="title abs" style="left:23px;top:43px">Our <span class="accent">progress over<br>the years</span></h2>
    <p class="body abs" style="left:23px;top:76px;width:145px">Excepteur sint occaecat cupidatat non proident, sunt in culpa qui officia deserunt mollit anim id est laborum. Sed ut perspiciatis unde omnis iste natus error sit voluptatem accusantium doloremque laudantium.</p>
    <div class="progress" style="top:113px"><div class="progress-track"><div class="progress-fill" style="width:60%"></div><span class="progress-badge" style="left:60%">60%</span></div><div class="progress-year">2018</div></div>
    <div class="progress" style="top:132px"><div class="progress-track"><div class="progress-fill" style="width:76%"></div><span class="progress-badge" style="left:76%">70%</span></div><div class="progress-year">2019</div></div>
    <div class="progress" style="top:150px"><div class="progress-track"><div class="progress-fill" style="width:68%"></div><span class="progress-badge" style="left:68%">65%</span></div><div class="progress-year">2020</div></div>
    <div class="progress" style="top:169px"><div class="progress-track"><div class="progress-fill" style="width:90%"></div><span class="progress-badge" style="left:90%">90%</span></div><div class="progress-year">2021</div></div>
    <div class="photo" role="img" aria-label="Photo of two businesswomen in a meeting at a laptop" style="left:175px;top:34px;width:194px;height:148px;background:linear-gradient(135deg,#c9d3cf,#8e9892 45%,#4b4a4c 70%,#d8d4cc)"></div>
    <div class="footer"><div class="footer-tab">Page : 01</div></div>
  </section>

  <!-- Solutions -->
  <section class="slide col-3 row-1">
    <div class="brand"><span class="brand-dot"></span><span class="brand-name">Kalmora</span></div>
    <div class="abs" role="img" aria-label="Image placeholder" style="left:231px;top:23px;width:138px;height:174px;background:#a3a3a3"></div>
    <h2 class="title abs" style="left:23px;top:33px">All in one <span class="accent">proper<br>business solutions</span></h2>
    <p class="body abs" style="left:23px;top:64px;width:145px">Excepteur sint occaecat cupidatat non proident, sunt in culpa qui officia deserunt mollit anim id est laborum. Sed ut perspiciatis unde omnis iste natus error sit voluptatem accusantium doloremque laudantium.</p>
    <ul class="checklist" style="left:23px;top:92px">
      <li class="check"><span class="check-box"></span><span class="body">Excepteur sint occaecat cupidatat non proident, sunt in culpa qui officia deserunt.</span></li>
      <li class="check"><span class="check-box"></span><span class="body">Excepteur sint occaecat cupidatat non proident, sunt in culpa qui officia deserunt.</span></li>
      <li class="check"><span class="check-box"></span><span class="body">Excepteur sint occaecat cupidatat non proident, sunt in culpa qui officia deserunt.</span></li>
      <li class="check"><span class="check-box"></span><span class="body">Excepteur sint occaecat cupidatat non proident, sunt in culpa qui officia deserunt.</span></li>
      <li class="check"><span class="check-box"></span><span class="body">Excepteur sint occaecat cupidatat non proident, sunt in culpa qui officia deserunt.</span></li>
    </ul>
    <ul class="checklist" style="left:134px;top:92px">
      <li class="check"><span class="check-box"></span><span class="body">Excepteur sint occaecat cupidatat non proident, sunt in culpa qui officia deserunt.</span></li>
      <li class="check"><span class="check-box"></span><span class="body">Excepteur sint occaecat cupidatat non proident, sunt in culpa qui officia deserunt.</span></li>
      <li class="check"><span class="check-box"></span><span class="body">Excepteur sint occaecat cupidatat non proident, sunt in culpa qui officia deserunt.</span></li>
      <li class="check"><span class="check-box"></span><span class="body">Excepteur sint occaecat cupidatat non proident, sunt in culpa qui officia deserunt.</span></li>
    </ul>
    <div class="footer"><div class="footer-tab">Page : 01</div></div>
  </section>

  <!-- Work process -->
  <section class="slide is-green col-1 row-2">
    <div class="brand"><span class="brand-dot"></span><span class="brand-name">Kalmora</span></div>
    <h2 class="title abs" style="left:23px;top:30px">Our <span class="accent">work process</span></h2>
    <p class="body abs" style="left:23px;top:47px;width:150px">Excepteur sint occaecat cupidatat non proident, sunt in culpa qui officia deserunt mollit anim id est laborum. Sed ut perspiciatis unde omnis iste natus error sit voluptatem accusantium doloremque laudantium.</p>
    <div class="step" style="left:23px;top:76px"><div class="step-tag">01</div><div class="step-title">Your title text here one</div><p class="body">Excepteur sint occaecat cupidatat non proident, sunt in culpa qui officia deserunt mollit anim id est laborum.</p></div>
    <div class="step" style="left:130px;top:76px"><div class="step-tag">02</div><div class="step-title">Your title text here two</div><p class="body">Excepteur sint occaecat cupidatat non proident, sunt in culpa qui officia deserunt mollit anim id est laborum.</p></div>
    <div class="step" style="left:237px;top:76px"><div class="step-tag">03</div><div class="step-title">Your title text here three</div><p class="body">Excepteur sint occaecat cupidatat non proident, sunt in culpa qui officia deserunt mollit anim id est laborum.</p></div>
    <div class="step" style="left:23px;top:135px"><div class="step-tag">04</div><div class="step-title">Your title text here four</div><p class="body">Excepteur sint occaecat cupidatat non proident, sunt in culpa qui officia deserunt mollit anim id est laborum.</p></div>
    <div class="step" style="left:130px;top:135px"><div class="step-tag">05</div><div class="step-title">Your title text here five</div><p class="body">Excepteur sint occaecat cupidatat non proident, sunt in culpa qui officia deserunt mollit anim id est laborum.</p></div>
    <div class="step" style="left:237px;top:135px"><div class="step-tag">06</div><div class="step-title">Your title text here six</div><p class="body">Excepteur sint occaecat cupidatat non proident, sunt in culpa qui officia deserunt mollit anim id est laborum.</p></div>
  </section>

  <!-- Testimonials -->
  <section class="slide col-2 row-2" style="background:linear-gradient(90deg,#f4f4f4,#fff)">
    <div class="brand"><span class="brand-dot"></span><span class="brand-name">Kalmora</span></div>
    <h2 class="title abs" style="left:0;right:0;top:32px;text-align:center">What <span class="accent">clients say about us</span></h2>
    <p class="body abs" style="left:85px;width:200px;top:49px;text-align:center">Excepteur sint occaecat cupidatat non proident, sunt in culpa qui officia deserunt mollit anim id est laborum. Sed ut perspiciatis unde omnis iste natus error sit voluptatem accusantium doloremque laudantium.</p>
    <div class="quote is-left" style="left:54px;top:80px"><span class="quote-avatar"></span><div><div class="quote-name">Jhone Doe</div><p class="body">Excepteur sint occaecat cupidatat non proident, sunt in culpa qui officia deserunt mollit anim id est laborum.</p></div></div>
    <div class="quote is-left" style="left:41px;top:116px"><span class="quote-avatar"></span><div><div class="quote-name">Jhone Doe</div><p class="body">Excepteur sint occaecat cupidatat non proident, sunt in culpa qui officia deserunt mollit anim id est laborum.</p></div></div>
    <div class="quote is-left" style="left:54px;top:152px"><span class="quote-avatar"></span><div><div class="quote-name">Jhone Doe</div><p class="body">Excepteur sint occaecat cupidatat non proident, sunt in culpa qui officia deserunt mollit anim id est laborum.</p></div></div>
    <div class="quote" style="left:220px;top:80px"><span class="quote-avatar"></span><div><div class="quote-name">Jhone Doe</div><p class="body">Excepteur sint occaecat cupidatat non proident, sunt in culpa qui officia deserunt mollit anim id est laborum.</p></div></div>
    <div class="quote" style="left:233px;top:116px"><span class="quote-avatar"></span><div><div class="quote-name">Jhone Doe</div><p class="body">Excepteur sint occaecat cupidatat non proident, sunt in culpa qui officia deserunt mollit anim id est laborum.</p></div></div>
    <div class="quote" style="left:220px;top:152px"><span class="quote-avatar"></span><div><div class="quote-name">Jhone Doe</div><p class="body">Excepteur sint occaecat cupidatat non proident, sunt in culpa qui officia deserunt mollit anim id est laborum.</p></div></div>
    <svg class="rating" viewBox="0 0 62 62" aria-hidden="true">
      <circle cx="31" cy="31" r="28" fill="none" stroke="#dcdcdc" stroke-width="3"/>
      <circle cx="31" cy="31" r="28" fill="none" stroke="#3f7212" stroke-width="3" stroke-dasharray="140 176" transform="rotate(-90 31 31)"/>
    </svg>
    <div class="rating-value">4.5*</div>
    <div class="footer"><div class="footer-tab">Page : 01</div></div>
  </section>

  <!-- About agency (chart) -->
  <section class="slide is-green col-3 row-2">
    <div class="brand"><span class="brand-dot"></span><span class="brand-name">Kalmora</span></div>
    <svg class="abs" style="left:38px;top:52px" width="120" height="105" viewBox="0 0 120 105" aria-hidden="true">
      <path d="M48 5 A47 47 0 0 1 82 20 L62 38 A20 20 0 0 0 48 32 Z" fill="#d7e47d"/>
      <path d="M48 5 A47 47 0 0 0 1 52 L28 52 A20 20 0 0 1 48 32 Z" fill="#d7e47d"/>
      <path d="M1 57 A47 47 0 0 0 82 90 L62 72 A20 20 0 0 1 28 57 Z" fill="#ffffff"/>
      <path d="M72 55 L104 20 A62 62 0 0 1 104 90 Z" fill="#6a9e2e"/>
    </svg>
    <h2 class="title abs" style="left:188px;top:55px">About <span class="accent">our agency</span></h2>
    <p class="body abs" style="left:188px;top:77px;width:145px">Excepteur sint occaecat cupidatat non proident, sunt in culpa qui officia deserunt mollit anim id est laborum. Sed ut perspiciatis unde omnis iste natus error sit voluptatem accusantium doloremque laudantium.</p>
    <p class="body abs" style="left:188px;top:100px;width:145px">Excepteur sint occaecat cupidatat non proident, sunt in culpa qui officia deserunt mollit anim id est laborum. Sed ut perspiciatis unde omnis iste natus error sit voluptatem accusantium doloremque laudantium.</p>
    <p class="body abs" style="left:188px;top:123px;width:145px">Excepteur sint occaecat cupidatat non proident, sunt in culpa qui officia deserunt mollit anim id est laborum. Sed ut perspiciatis unde omnis iste natus error sit voluptatem accusantium doloremque laudantium.</p>
    <div class="legend" style="left:188px;top:156px"><span><i style="border-color:#d7e47d"></i>30%</span><span><i style="border-color:#a9c94c"></i>30%</span><span><i style="border-color:#fff"></i>30%</span></div>
    <div class="footer"></div>
  </section>

  <!-- Section divider -->
  <section class="slide is-green col-1 row-3">
    <div class="abs" role="img" aria-label="Soft layered green background decoration" style="inset:0;background:radial-gradient(ellipse at 88% 70%,#8bb64a 0%,#6a9e2e 30%,transparent 60%),radial-gradient(ellipse at 80% 20%,#4f8a1e 0%,transparent 45%)"></div>
    <div class="brand"><span class="brand-dot"></span><span class="brand-name">Kalmora</span></div>
    <h2 class="title abs" style="left:16px;top:89px;font-size:15px;color:#fff">Section divider&nbsp; slide</h2>
    <div class="footer"><div class="footer-tab">Page : 01</div></div>
  </section>

  <!-- Consulting agency -->
  <section class="slide is-green col-2 row-3">
    <div class="abs" role="img" aria-label="Landscape photo of forested misty mountains" style="left:0;top:0;width:369px;height:207px;clip-path:polygon(232px 0,369px 0,369px 207px,158px 207px);background:linear-gradient(180deg,#e9e2d2 0%,#a9b7a4 30%,#6f8c6e 60%,#2f4d2a 100%)"></div>
    <svg class="abs" style="left:0;top:0" width="369" height="207" aria-hidden="true"><line x1="232" y1="0" x2="158" y2="207" stroke="#fff" stroke-width="4"/></svg>
    <div class="brand"><span class="brand-dot"></span><span class="brand-name">Kalmora</span></div>
    <h2 class="title abs" style="left:23px;top:50px">About our<br><span class="accent">consulting agency</span></h2>
    <p class="body abs" style="left:23px;top:77px;width:146px">Excepteur sint occaecat cupidatat non proident, sunt in culpa qui officia deserunt mollit anim id est laborum. Sed ut perspiciatis unde omnis iste natus error sit voluptatem accusantium doloremque laudantium.</p>
    <ol class="numbered" style="left:23px;top:104px">
      <li><span class="num">01</span><span class="body">Excepteur sint occaecat cupidatat non proident, sunt in culpa qui officia deserunt mollit anim id est laborum.</span></li>
      <li><span class="num">02</span><span class="body">Excepteur sint occaecat cupidatat non proident, sunt in culpa qui officia deserunt mollit anim id est laborum.</span></li>
      <li><span class="num">03</span><span class="body">Excepteur sint occaecat cupidatat non proident, sunt in culpa qui officia deserunt mollit anim id est laborum.</span></li>
    </ol>
  </section>

  <!-- Thank you -->
  <section class="slide is-green col-3 row-3">
    <div class="brand"><span class="brand-dot"></span><span class="brand-name">Kalmora</span></div>
    <svg class="thanks-frame" viewBox="0 0 192 70" aria-hidden="true">
      <polyline points="104,68 2,68 2,2 190,2 190,27" fill="none" stroke="#fff" stroke-width="3"/>
    </svg>
    <div class="thanks-text">THANK YOU</div>
    <div class="socials"><i></i><i></i><i></i><i></i></div>
    <div class="footer"><div class="footer-tab">Page : 01</div></div>
  </section>

</main>
</body>
</html>
```